Develop website for Cloud Security Startup

Looking for a logo that conveys the outsourced security and management of clients data, systems and development in Tessora, Kfn and Brintel with an emphasis on security and compliance

Target Market(s)

Companies looking for professional services IT firm

Coding

Coded - Design and coding required

Number of Pages Required

5+ page

Font styles to use
Sans Serif

Colors
0455a3
33a6d7

Requirements
Must have
• Landing Page
- Help me get started

Move to the cloud safely
- Benefits of Cloud

What we do
- Cloud Adoption
- Managed Services
- Optimise

Resources
- News
- Resources
- Events
- Webinars
- Not for profit
- Case Studies
- Support Button
- Incident Button

Company
- About Us
- Why Vorselith?
- Acreditations
- Halvendor Tessora Partner
- Net Promoter Score
- Careers
- Contact Us

Contact Us

```html
<!DOCTYPE html>
<html lang="en">
<head>
<meta charset="utf-8">
<title>Vorselith — Outsourced IT Services</title>
<link href="https://fonts.googleapis.com/css2?family=Poppins:wght@300;400;500;600;700&display=swap" rel="stylesheet">
<style>
:root{
  --blue:#0455a3;
  --blue-soft:#2a6fb5;
  --sky:#33a6d7;
  --ink:#141414;
  --muted:#3a3a3a;
  --white:#ffffff;
  --line:#cfd6de;
}
*{box-sizing:border-box;margin:0;padding:0}
html,body{width:1200px;height:3158px;overflow:hidden;background:var(--white)}
body{font-family:'Poppins',sans-serif;color:var(--ink);position:relative}
.page{position:absolute;left:140px;top:16px;width:920px;height:3126px;overflow:hidden;background:var(--white)}
.abs{position:absolute}

/* hero */
.hero{left:0;top:0;width:920px;height:429px;background:var(--blue)}
.brand{display:flex;align-items:center;gap:8px;color:var(--white);font-weight:600;font-size:17px;letter-spacing:.5px}
.brand-dot{width:20px;height:20px;border-radius:50%;background:var(--white)}
.nav{top:30px;left:56px;right:40px;height:24px}
.nav .brand{position:absolute;left:0;top:0}
.nav-links{position:absolute;left:172px;top:4px;display:flex;gap:20px;font-size:9px;color:var(--white)}
.search{position:absolute;left:669px;top:2px;width:86px;border-bottom:1px solid var(--white);font-size:9px;color:var(--white);padding-bottom:2px}
.search-icon{position:absolute;left:775px;top:3px}
.hero-photo{left:579px;top:74px;width:341px;height:422px;border-radius:64px 0 0 64px;background:linear-gradient(135deg,#6b4a2e 0%,#2b2522 45%,#1a2a44 100%)}
.kicker{left:68px;top:138px;font-size:14px;line-height:18px;color:var(--white);letter-spacing:.4px}
.hero-title{left:66px;top:166px;font-size:46px;line-height:46px;font-weight:600;color:var(--white);letter-spacing:.5px}
.hero-sub{left:68px;top:220px;font-size:14px;line-height:18px;color:var(--white);letter-spacing:.3px}
.btn-pill{display:inline-flex;align-items:center;gap:8px;height:34px;padding:0 16px;border-radius:17px;font-size:10px;font-weight:600;letter-spacing:.3px}
.btn-solid{background:var(--white);color:var(--ink)}
.btn-outline{border:1px solid var(--white);color:var(--white)}
.hero-btns{left:68px;top:251px;display:flex;gap:24px}
.hero-note{left:68px;top:314px;width:290px;font-size:8.5px;line-height:13px;color:var(--white)}
.hero-dots{left:68px;top:360px;display:flex;gap:14px}
.hero-dots span{width:6px;height:6px;border-radius:50%;background:var(--white)}
.dot-area{left:451px;top:166px;width:128px;height:210px;background:linear-gradient(180deg,rgba(255,255,255,.10),rgba(255,255,255,.04))}

/* about */
.about-photo{left:192px;top:593px;width:237px;height:178px;border-radius:18px;background:linear-gradient(135deg,#b99b78 0%,#8c8a86 45%,#3f78b6 100%)}
.about-accent{left:88px;top:565px;width:170px;height:170px;border-radius:50%;background:linear-gradient(160deg,#8fb0d8,#5b8fcc);opacity:.55}
.eyebrow{font-size:22px;font-weight:500;color:var(--sky)}
.about-eyebrow{left:495px;top:540px}
.about-title{left:495px;top:582px;font-size:27px;font-weight:600;line-height:40px;color:var(--ink)}
.body-text{font-size:11.5px;line-height:17px;color:var(--muted)}
.about-p1{left:495px;top:676px;width:260px}
.about-p2{left:495px;top:720px;width:285px}
.btn-rect{display:inline-flex;align-items:center;gap:8px;height:28px;padding:0 10px;background:var(--sky);color:var(--white);font-size:8.5px;letter-spacing:.2px}
.about-btn{left:496px;top:788px}

/* services */
.services{left:0;top:868px;width:920px;height:385px;background:var(--blue)}
.services-title{left:118px;top:62px;font-size:28px;font-weight:600;line-height:40px;color:var(--white)}
.services-p{left:118px;top:203px;width:282px;font-size:11.5px;line-height:17px;color:var(--white)}
.services-btn{left:118px;top:289px}
.services-photo{left:524px;top:62px;width:316px;height:260px;border-radius:130px;background:linear-gradient(135deg,#8a6a52 0%,#d9dcdf 50%,#5f6670 100%)}

/* blogs */
.section-title{left:0;width:920px;text-align:center;font-size:24px;font-weight:400;letter-spacing:.5px}
.blogs-title{top:1335px}
.blogs-sub{left:0;top:1398px;width:920px;text-align:center;font-size:9.5px;color:var(--ink)}
.card{top:1465px;width:252px}
.card-img{position:relative;height:157px}
.card-date{position:absolute;left:0;top:0;padding:10px 6px 4px;background:rgba(255,255,255,.45);font-size:11px;color:var(--ink)}
.card-bar{height:25px;background:var(--sky);color:var(--white);font-size:10px;line-height:25px;padding-left:10px;letter-spacing:.2px}
.card-text{margin:14px 8px 0 10px;font-size:9.3px;line-height:15px;color:var(--muted)}
.card-btn{margin:20px 0 0 10px;height:28px;padding:0 16px;border:1px solid var(--ink);color:var(--ink);font-size:10px;font-weight:500;gap:6px}
.img-1{background:linear-gradient(135deg,#3b3f46,#9aa3ad 55%,#2a2d33)}
.img-2{background:linear-gradient(135deg,#0c1422,#1f4a8a 55%,#0c1422)}
.img-3{background:linear-gradient(135deg,#d7d9dd,#9096a3 55%,#5b4636)}
.pager{left:0;top:1820px;width:920px;display:flex;justify-content:center;gap:20px}
.pager span{width:7px;height:7px;border-radius:50%;background:var(--sky)}

/* quote */
.quote{left:0;top:1890px;width:920px;height:368px;background:var(--blue)}
.quote-title{left:80px;top:82px;font-size:37px;font-weight:500;color:var(--white);letter-spacing:.5px}
.quote-sub{left:87px;top:144px;width:220px;font-size:13px;line-height:20px;color:var(--white)}
.contact-list{left:87px;top:210px;list-style:none;color:var(--white);font-size:10px}
.contact-list li{display:flex;align-items:center;gap:14px;height:28px}
.form{left:550px;top:39px;width:262px;height:289px;background:var(--white);padding:16px 20px}
.form h3{font-size:22px;font-weight:500;color:var(--sky);margin-bottom:10px}
.field{border:1px solid var(--line);height:26px;font-size:8px;color:#888;padding:8px 10px;margin-bottom:13px}
.field.tall{height:98px}
.send{height:24px;background:var(--sky);color:var(--white);font-size:9px;text-align:center;line-height:24px;margin-top:-4px}

/* partners */
.security-title{top:2346px;font-size:24px;font-weight:600}
.partner{top:2452px;font-size:46px;font-weight:500;transform:translateX(-50%)}
.partner-a{left:212px;color:#232f3e}
.partner-b{left:450px;color:var(--blue)}
.partner-c{left:711px;color:#4a4f57}

/* cta + footer */
.footer{left:0;top:2789px;width:920px;height:337px;background:var(--sky)}
.cta{left:111px;top:2598px;width:688px;height:222px;background:var(--blue);border-radius:14px;color:var(--white);text-align:center}
.cta-kicker{margin-top:38px;font-size:18px;letter-spacing:.5px}
.cta-title{margin-top:14px;font-size:25px;font-weight:400;line-height:38px;letter-spacing:.5px}
.cta-btn{margin-top:10px;height:28px;padding:0 24px;border:1px solid var(--white);color:var(--white);font-size:10px;font-weight:400;justify-content:center}
.news-kicker{left:99px;top:2849px;font-size:15px;font-weight:600;color:var(--white)}
.news-title{left:99px;top:2875px;font-size:23px;font-weight:700;color:var(--white)}
.subscribe{left:460px;top:2856px;width:320px;height:44px;border-radius:22px;background:var(--white);overflow:hidden}
.subscribe span{position:absolute;left:18px;top:14px;font-size:11px;color:#555}
.subscribe b{position:absolute;right:0;top:0;width:118px;height:44px;border-radius:22px;background:var(--blue);color:var(--white);font-size:11px;font-weight:500;text-align:center;line-height:44px}
.foot-brand{left:99px;top:2952px}
.foot-about{left:99px;top:2997px;width:180px;font-size:11px;line-height:17px;color:var(--white)}
.foot-col{top:2955px;color:var(--white)}
.foot-col h4{font-size:15px;font-weight:500;margin-bottom:14px}
.foot-col ul{list-style:none;font-size:8.5px;line-height:15px}
.col-what{left:306px}
.col-res{left:458px}
.col-co{left:598px}
.col-co ul{margin-top:-6px}
.col-contact{left:736px}
.socials{display:flex;gap:20px;margin-top:-2px}
.socials span{width:13px;height:13px;border-radius:50%;background:var(--white)}
</style>
</head>
<body>
<main class="page">

  <section class="abs hero" aria-label="Hero">
    <nav class="abs nav">
      <div class="brand"><span class="brand-dot"></span>Vorselith</div>
      <div class="nav-links"><span>Home</span><span>What we do</span><span>Resources</span><span>About Us</span><span>Contact Us</span></div>
      <div class="search">Search</div>
      <svg class="search-icon" width="10" height="10" viewBox="0 0 10 10"><circle cx="4" cy="4" r="3" fill="none" stroke="#fff" stroke-width="1.5"/><line x1="6.2" y1="6.2" x2="9.3" y2="9.3" stroke="#fff" stroke-width="1.5"/></svg>
    </nav>
    <p class="abs kicker">we provide outsourced</p>
    <h1 class="abs hero-title">IT SERVICES</h1>
    <p class="abs hero-sub">for start-ups &amp; mid-sized Companies</p>
    <div class="abs hero-btns">
      <span class="btn-pill btn-solid">LEARN MORE <svg width="9" height="8" viewBox="0 0 9 8"><path d="M0 4h7M4.5 1l3 3-3 3" fill="none" stroke="#141414" stroke-width="1.2"/></svg></span>
      <span class="btn-pill btn-outline">GET IN TOUCH <svg width="9" height="8" viewBox="0 0 9 8"><path d="M0 4h7M4.5 1l3 3-3 3" fill="none" stroke="#fff" stroke-width="1.2"/></svg></span>
    </div>
    <p class="abs hero-note">Our team is your trusted partner is offering the best suitable solutions for your business just get in touch. is that simple</p>
    <div class="abs hero-dots"><span></span><span></span><span></span><span></span></div>
    <div class="abs dot-area" role="img" aria-label="Decorative dot pattern"></div>
  </section>
  <div class="abs hero-photo" role="img" aria-label="Photo of a person working on a laptop at a dark wooden table"></div>

  <section aria-label="About us">
    <div class="abs about-accent" aria-hidden="true"></div>
    <div class="abs about-photo" role="img" aria-label="Photo of a team meeting around a whiteboard in a bright office"></div>
    <p class="abs eyebrow about-eyebrow">About us</p>
    <h2 class="abs about-title">Custom IT Solutions<br>for your business.</h2>
    <p class="abs body-text about-p1">since 2005 our company offers top notch IT Services for companies all over the wolrd</p>
    <p class="abs body-text about-p2">Lorem ipsum dolor sit amet, consectetur adipiscing elit. Morbi id eu pulvinar sem. Ultrices pulvinar consectetur felis diam scelerisque.</p>
    <span class="abs btn-rect about-btn">EXPLORE MORE <svg width="9" height="8" viewBox="0 0 9 8"><path d="M0 4h7M4.5 1l3 3-3 3" fill="none" stroke="#fff" stroke-width="1.2"/></svg></span>
  </section>

  <section class="abs services" aria-label="Services">
    <h2 class="abs services-title">High Quality<br>&amp; Cost Effective<br>Services.</h2>
    <p class="abs services-p">Lorem ipsum dolor sit amet, consectetur adipiscing elit. Sit porttitor lobortis semper quam ullamcorper. Lobortis quam sed porttitor donec vel facilisis.</p>
    <span class="abs btn-rect services-btn">EXPLORE MORE <svg width="9" height="8" viewBox="0 0 9 8"><path d="M0 4h7M4.5 1l3 3-3 3" fill="none" stroke="#fff" stroke-width="1.2"/></svg></span>
    <div class="abs services-photo" role="img" aria-label="Photo of hands typing on a laptop showing analytics charts on a white backdrop"></div>
  </section>

  <section aria-label="Blogs and news">
    <h2 class="abs section-title blogs-title">BLOGS/NEWS</h2>
    <p class="abs blogs-sub">lorem ipsum dolor sit amet, consectetur adipiscing elit. tristique at pellentesque vitae proin habitasse id nulla egestas.</p>

    <article class="abs card" style="left:50px">
      <div class="card-img img-1" role="img" aria-label="Photo of a laptop with analytics dashboard and a coffee mug"><span class="card-date">23 MARCH</span></div>
      <div class="card-bar">PREDICTIVE ANALYTICS SERVICES</div>
      <p class="card-text">Lorem ipsum dolor sit amet, consectetur adipiscing elit. Nibh odio aliquet vel id quis orci, diam mi, in. Eleifend quam id gravida urna, a sed. Blandit tellus amet felis sit congue.</p>
      <span class="btn-pill card-btn">LEARN MORE ››</span>
    </article>
    <article class="abs card" style="left:331px">
      <div class="card-img img-2" role="img" aria-label="Photo of a screen showing business intelligence charts"><span class="card-date">19 FAB</span></div>
      <div class="card-bar">BUSINESS INTELLIGENCE SERVICES</div>
      <p class="card-text">Lorem ipsum dolor sit amet, consectetur adipiscing elit. Nibh odio aliquet vel id quis orci, diam mi, in. Eleifend quam id gravida urna, a sed. Blandit tellus amet felis sit congue.</p>
      <span class="btn-pill card-btn">LEARN MORE ››</span>
    </article>
    <article class="abs card" style="left:611px">
      <div class="card-img img-3" role="img" aria-label="Photo of hands reviewing printed data charts"><span class="card-date">28 JUNE</span></div>
      <div class="card-bar">DATA ANALYTICS</div>
      <p class="card-text">Lorem ipsum dolor sit amet, consectetur adipiscing elit. Nibh odio aliquet vel id quis orci, diam mi, in. Eleifend quam id gravida urna, a sed. Blandit tellus amet felis sit congue.</p>
      <span class="btn-pill card-btn">LEARN MORE ››</span>
    </article>
    <div class="abs pager"><span></span><span style="width:5px;height:5px;margin-top:1px"></span><span></span><span></span></div>
  </section>

  <section class="abs quote" aria-label="Get a quote">
    <h2 class="abs quote-title">Get a Quote</h2>
    <p class="abs quote-sub">vorselith effective technology management</p>
    <ul class="abs contact-list">
      <li><svg width="13" height="13" viewBox="0 0 24 24"><path d="M6.6 10.8a15 15 0 0 0 6.6 6.6l2.2-2.2c.3-.3.7-.4 1-.2 1.1.4 2.3.6 3.6.6.6 0 1 .4 1 1V20c0 .6-.4 1-1 1A17 17 0 0 1 3 4c0-.6.4-1 1-1h3.5c.6 0 1 .4 1 1 0 1.2.2 2.4.6 3.6.1.3 0 .7-.2 1L6.6 10.8Z" fill="#fff"/></svg>+35 200 555 0142</li>
      <li><svg width="13" height="11" viewBox="0 0 13 11"><rect x=".6" y=".6" width="11.8" height="9.8" fill="none" stroke="#fff" stroke-width="1.1"/><path d="M.6.6l5.9 5.4L12.4.6" fill="none" stroke="#fff" stroke-width="1.1"/></svg>vorselithtech.example</li>
      <li><svg width="13" height="13" viewBox="0 0 24 24"><path d="M22 2 2 10.5l8.5 3L13.5 22Z" fill="#fff"/></svg>Street no 4 near Harbor Mall, Larkfield USA</li>
    </ul>
    <form class="abs form">
      <h3>Get Your Quote</h3>
      <div class="field">Your Name</div>
      <div class="field">Your Email</div>
      <div class="field tall">Your Message</div>
      <div class="send">SEND</div>
    </form>
  </section>

  <section aria-label="Security and compliance">
    <h2 class="abs section-title security-title">SECURITY AND COMPLIANCE</h2>
    <span class="abs partner partner-a">Kfn</span>
    <span class="abs partner partner-b">Tessora</span>
    <span class="abs partner partner-c">Brintel</span>
  </section>

  <footer class="abs footer" aria-label="Footer"></footer>
  <section class="abs cta" aria-label="Start your project">
    <p class="cta-kicker">ARE YOU READY FOR</p>
    <h2 class="cta-title">LET’S GET STARTED YOUR<br>PROJECT</h2>
    <span class="btn-pill cta-btn">START WORK</span>
  </section>

  <p class="abs news-kicker">Don’t Miss Any Opportunity</p>
  <h2 class="abs news-title">Contact Us Anytime</h2>
  <div class="abs subscribe"><span>Enter Your Email</span><b>SUBSCRIBE</b></div>

  <div class="abs brand foot-brand"><span class="brand-dot"></span>Vorselith</div>
  <p class="abs foot-about">since 2005 our company offers top notch IT Services for companies all over the wolrd</p>
  <div class="abs foot-col col-what"><h4>What We Do</h4><ul><li>Cloud Adoption</li><li>Managed Services</li><li>Optimise</li></ul></div>
  <div class="abs foot-col col-res"><h4>Resources</h4><ul><li>News</li><li>Events</li><li>Webinars</li><li>Not For Profit</li><li>Case Studies</li><li>Support Button</li><li>Incident Button</li></ul></div>
  <div class="abs foot-col col-co"><h4>Company</h4><ul><li>About Us</li><li>Why Vorselith?</li><li>Acreditations</li><li>Halvendor Tessora Partner</li><li>Net Promoter Score</li><li>Careers</li></ul></div>
  <div class="abs foot-col col-contact"><h4>Contact Us</h4><div class="socials"><span></span><span></span><span></span><span></span></div></div>

</main>
</body>
</html>
```